Quiet Harbors Brochure

Bi fold brochure outlining company, 3 products -variety of uses (for beauty industry)brochure should fit into 6x9 envelope,

Target Market(s)

nail tech's

Industry/Entity Type

Beauty

Colors
6a429a
1b1b1b
ebebeb

Requirements
Must have
• 3 pictures of my products, description and content . table towels (flat) roll towels and 4x4 squares
Nice to have
• clean lines, mirror similarly to https://quietharborslinens.com/home/1-roll-table-towel . I want it to have similar clean lines like the label on this roll. I am a geometric person so if you want to have shapes to add it must be purple black and white
Should not have
• i included my trifold brochure of which i am updating. the one i included with the polka dots was something i did on canva but the wording is best on this.

```html
<!DOCTYPE html>
<html lang="en">
<head>
<meta charset="utf-8">
<title>Quiet Harbors Brochure</title>
<link href="https://fonts.googleapis.com/css2?family=Quicksand:wght@600;700&family=Open+Sans:wght@400;600;700;800&display=swap" rel="stylesheet">
<style>
:root{
  --purple:#6a429a;
  --purple-deep:#4b2a7a;
  --purple-light:#9b72c9;
  --purple-soft:#b79bd6;
  --ink:#1b1b1b;
  --paper:#ebebeb;
  --white:#ffffff;
  --stage:#a9a9a9;
}
*{margin:0;padding:0;box-sizing:border-box}
html,body{width:989px;height:1200px;overflow:hidden}
body{background:var(--stage);font-family:"Open Sans",sans-serif;position:relative}
.page{position:absolute;top:300px;width:400px;height:600px;overflow:hidden;background:var(--paper);box-shadow:0 4px 14px rgba(0,0,0,.25)}
.page--front{left:64px}
.page--back{left:524px}
.page svg.page__shapes{position:absolute;inset:0}
.abs{position:absolute}
.headline{font-family:"Quicksand",sans-serif;font-weight:700}

/* brand */
.brand{display:flex;align-items:center;gap:10px}
.brand__name{font-family:"Open Sans",sans-serif;font-weight:800;line-height:.95;color:var(--ink)}
.brand__mark{background:var(--purple-soft)}

/* front */
.front-brand{top:30px;right:32px}
.front-brand .brand__name{font-size:32px}
.front-brand .brand__mark{width:62px;height:62px}
.photo{position:absolute;top:170px;left:214px;width:186px;height:200px;background:linear-gradient(100deg,rgba(235,235,235,0) 0%,#d9c3b1 35%,#a37c62 75%,#7a5744 100%)}
.feature{top:192px;left:12px}
.feature__title{font-size:22px;color:var(--purple);letter-spacing:.5px;line-height:1.1}
.feature__sub{font-size:11px;color:var(--ink);margin-top:2px}
.tagline{top:245px;left:12px}
.tagline__main{font-family:"Open Sans",sans-serif;font-weight:800;font-size:17px;color:var(--ink);line-height:1}
.tagline__small{font-size:6px;color:var(--purple);margin-top:4px}
.product{position:absolute;width:110px;height:110px;border-radius:50%;background:var(--white);box-shadow:0 2px 6px rgba(0,0,0,.25)}
.product__img{position:absolute;inset:8px;border-radius:50%;border:2px dotted var(--purple);background:radial-gradient(circle,#f7f7f7 30%,#dcdcdc 100%)}
.product--flat{left:29px;top:300px}
.product--square{left:147px;top:300px}
.product--roll{left:264px;top:300px}
.best{top:414px;left:0;width:400px;text-align:center;color:var(--white);font-size:29px;line-height:1.3;letter-spacing:.5px}
.industry{top:496px;left:0;width:400px;display:flex;align-items:center;justify-content:center;gap:8px;color:var(--purple-light);font-size:13px}
.industry span.rule{display:block;width:40px;height:1px;background:#888}
.phone-pill{top:522px;left:110px;width:180px;height:26px;border-radius:13px;background:var(--purple);color:var(--white);font-weight:700;font-size:14px;display:flex;align-items:center;justify-content:center;gap:6px;border:1px solid #c9b3e3}
.front-url{top:556px;left:0;width:400px;text-align:center;color:#bdbdbd;font-size:8px}

/* back */
.shows{top:82px;left:0;width:400px;text-align:center;color:var(--purple);font-size:25px;line-height:1.32;letter-spacing:.8px}
.show-list{top:203px;left:0;width:400px;text-align:center;list-style:none;font-size:11px;font-weight:700;color:var(--ink);line-height:1.42}
.back-url{top:318px;left:0;width:400px;text-align:center;color:var(--purple);font-weight:700;font-size:13px}
.back-brand{top:392px;left:0;width:400px;justify-content:center}
.back-brand .brand__name{font-size:26px;color:var(--white)}
.back-brand .brand__mark{width:44px;height:44px}
.contact-icons{top:468px;left:0;width:400px;display:flex;justify-content:center;gap:4px}
.contact-icons span{width:14px;height:14px;border-radius:50%;background:var(--white);display:flex;align-items:center;justify-content:center}
.office{top:490px;left:0;width:400px;text-align:center;color:var(--white);font-size:9px;line-height:1.4}
.office strong{font-weight:700;font-size:10px}
.social{top:570px;left:0;width:400px;display:flex;justify-content:center;gap:6px}
.social span{width:8px;height:8px;border-radius:50%;background:var(--white)}
</style>
</head>
<body>

<!-- FRONT PAGE -->
<section class="page page--front">
  <svg class="page__shapes" width="400" height="600" viewBox="0 0 400 600">
    <defs>
      <linearGradient id="paperFront" x1="0" y1="0" x2="1" y2="1">
        <stop offset="0" stop-color="#fafafa"/><stop offset="1" stop-color="#e4e4e4"/>
      </linearGradient>
      <linearGradient id="swoopFront" x1="0" y1="0" x2="1" y2="0">
        <stop offset="0" stop-color="#4b2a7a"/><stop offset="1" stop-color="#7a52ae"/>
      </linearGradient>
    </defs>
    <rect width="400" height="600" fill="url(#paperFront)"/>
    <path d="M0,0 L40,0 C110,80 250,128 400,112 L400,128 C250,148 100,110 0,60 Z" fill="url(#swoopFront)"/>
    <path d="M0,66 C100,118 250,154 400,134" fill="none" stroke="#1b1b1b" stroke-width="3"/>
    <rect x="0" y="367" width="400" height="233" fill="#1b1b1b"/>
  </svg>

  <div class="brand front-brand abs">
    <div class="brand__name">Quiet<br>Harbors</div>
    <div class="brand__mark"></div>
  </div>

  <div class="photo" role="img" aria-label="Smiling woman lifting a disposable towel from over her eyes"></div>

  <div class="feature abs">
    <div class="feature__title headline">USE WET OR DRY</div>
    <div class="feature__sub">WILL WITHSTAND HEAT</div>
  </div>
  <div class="tagline abs">
    <div class="tagline__main">Pure Comfort<br>Daily</div>
    <div class="tagline__small">Gentle on skin. Easy to toss.</div>
  </div>

  <div class="product product--flat"><div class="product__img" role="img" aria-label="Packaged flat table towels"></div></div>
  <div class="product product--square"><div class="product__img" role="img" aria-label="Stack of 4x4 towel squares"></div></div>
  <div class="product product--roll"><div class="product__img" role="img" aria-label="Roll of table towels"></div></div>

  <h1 class="best abs headline">THE BEST<br>DISPOSABLE TOWEL</h1>
  <div class="industry abs"><span class="rule"></span>In The Beauty And Spa Industry<span class="rule"></span></div>
  <div class="phone-pill abs">
    <svg width="13" height="13" viewBox="0 0 24 24"><circle cx="12" cy="12" r="12" fill="#fff"/><path d="M8 6l2 0 1 3-1.5 1a7 7 0 0 0 4 4l1-1.5 3 1 0 2a2 2 0 0 1-2 2A11 11 0 0 1 6 8a2 2 0 0 1 2-2z" fill="#6a429a"/></svg>
    (555) 214-3080
  </div>
  <div class="front-url abs">www.quietharborslinens.com</div>
</section>

<!-- BACK PAGE -->
<section class="page page--back">
  <svg class="page__shapes" width="400" height="600" viewBox="0 0 400 600">
    <defs>
      <linearGradient id="bandBack" x1="0" y1="0" x2="1" y2="0">
        <stop offset="0" stop-color="#4b2a7a"/><stop offset="1" stop-color="#9b72c9"/>
      </linearGradient>
      <linearGradient id="paperBack" x1="0" y1="0" x2="0" y2="1">
        <stop offset="0" stop-color="#ffffff"/><stop offset="1" stop-color="#e8e8e8"/>
      </linearGradient>
    </defs>
    <rect width="400" height="600" fill="#1b1b1b"/>
    <rect width="400" height="110" fill="url(#bandBack)"/>
    <circle cx="67" cy="377" r="42" fill="#6a429a" opacity=".8"/>
    <path d="M0,100 C120,62 270,58 400,70 L400,352 L120,352 C90,352 80,383 48,383 Q0,383 0,335 Z" fill="url(#paperBack)"/>
    <path d="M0,100 C120,62 270,58 400,70" fill="none" stroke="#1b1b1b" stroke-width="4"/>
    <circle cx="340" cy="535" r="22" fill="none" stroke="#fff" stroke-width="1.5"/>
  </svg>

  <h2 class="shows abs headline">AVAILABLE ONLINE<br>OR TRADE SHOWS<br>COME SEE US @</h2>
  <ul class="show-list abs">
    <li>LONE STAR NAIL SHOW</li>
    <li>COASTLINE NAIL PRO</li>
    <li>CASCADE NAIL EXPO</li>
    <li>NAIL TECH SUMMIT OF THE RIDGE</li>
    <li>VALLEY NAIL PRO</li>
    <li>CANYON NAIL EXPO</li>
  </ul>
  <div class="back-url abs">www.quietharborslinens.com</div>

  <div class="brand back-brand abs">
    <div class="brand__name">Quiet<br>Harbors</div>
    <div class="brand__mark"></div>
  </div>

  <div class="contact-icons abs">
    <span><svg width="8" height="8" viewBox="0 0 24 24"><path d="M12 2a7 7 0 0 0-7 7c0 5 7 13 7 13s7-8 7-13a7 7 0 0 0-7-7zm0 9.5A2.5 2.5 0 1 1 12 6.5a2.5 2.5 0 0 1 0 5z" fill="#6a429a"/></svg></span>
    <span><svg width="8" height="8" viewBox="0 0 24 24"><path d="M6 3l3 0 2 5-2 1.5a10 10 0 0 0 5.5 5.5L16 13l5 2 0 3a3 3 0 0 1-3 3A16 16 0 0 1 3 6a3 3 0 0 1 3-3z" fill="#6a429a"/></svg></span>
    <span><svg width="8" height="8" viewBox="0 0 24 24"><rect x="2" y="5" width="20" height="14" rx="2" fill="#6a429a"/><path d="M2 6l10 7 10-7" fill="none" stroke="#fff" stroke-width="2"/></svg></span>
  </div>
  <div class="office abs">
    <strong>OUR OFFICE</strong><br>
    Quiet Harbors Towels<br>
    P.O. Box 4410 Harbor Point, AZ 85010<br>
    (555) 214-3080<br>
    (555) 214-3091
  </div>
  <div class="social abs"><span></span><span></span><span></span></div>
</section>

</body>
</html>
```